National Sales Conference

We need a cool one page flyer inviting our sales partners to a National Sales Training Class.

Most important event in 5 years! Do not even consider missing it

Details of Sales Meeting
Nov 10th - 11th in Dallas, TX
Nov 10th (welcome party) 7-9pm

Preliminary Agenda
Nov, 10th 7-9pm Welcome Reception

Nov 11th and 12th 9-4 Cardwise Drill Week Sales training. Learn the tools you need to become more relevant in the marketplace as we launch multiple new cutting edge products and services. Many vendors will be on hand to personally meet you and provide the tools and marketing information you need.

Location of event
Northgate Harbor Inn East
2870 Lanterly Pkwy.
Fort Worth, TX 76192
FREE Shuttle from NHE!
Updates

Please put the Corvell Vendor Solutions logo at the TOP left and the Bristane Ledger logo make it small and near the bottom

Add the following TEXT. 

*** This event is so important our CEO, Marcus Odrey has decided that we are covering all of the expenses! That's right, we will provide the sleeping room based on double occupancy, all meals, and with 10 deals in 90 days we will even reimburse your airfare if a flight is necessary. 

Be sure to include the RSVP information and lines for the to print out and check if they are coming or not as indicated in the original brief. 

This flyer will be sent to our sales agents VIA Email in PDF. Therefore, if we need to make it 2 pages so it is not so cluttered, I'm okay with that. 

Target Market(s)

Our Sales Agents

Industry/Entity Type

Training

Requirements
Must have
• One page! High energy will a strong call to action.
• Needs a small fill in the blank for an RSVP
• Name _______________
• Check Box YES! I will gladly attend. _____ # attending
• Check Box Can't make it.
• Fax RSVP to 775-555-0143 or email marcuso@corvellhq.example

```html
<!DOCTYPE html>
<html lang="en">
<head>
<meta charset="utf-8">
<title>National Sales Conference Flyer</title>
<link rel="stylesheet" href="https://fonts.googleapis.com/css2?family=Anton&family=Cinzel:wght@700&family=Open+Sans:wght@300;400;600&display=swap">
<style>
  :root {
    --brand-blue: #1b74c8;
    --soft-blue: #3b86d4;
    --location-blue: #3c79c6;
    --lime: #8dc21f;
    --ink: #111111;
    --white: #ffffff;
    --paper: #ffffff;
    --photo-light: #eef1f4;
    --photo-mid: #c9d0d8;
    --chart-bar: #eceef1;
    --chart-arrow: #f3d4d4;
  }
  * { box-sizing: border-box; margin: 0; padding: 0; }
  html, body { width: 1200px; height: 778px; overflow: hidden; background: var(--paper); }
  body { font-family: "Open Sans", Arial, sans-serif; position: relative; }

  .spread { position: relative; width: 1200px; height: 778px; }
  .page { position: absolute; top: 0; width: 600px; height: 778px; }
  .page--cover { left: 0; }
  .page--agenda { left: 600px; }

  .brand { position: absolute; display: flex; align-items: center; gap: 8px; white-space: nowrap;
           font-family: "Open Sans", Arial, sans-serif; font-weight: 600; color: var(--brand-blue); }
  .brand--lead { font-size: 19px; }
  .brand--lead .brand__mark { width: 22px; height: 22px; background: var(--brand-blue); }
  .brand--small { font-size: 11px; gap: 5px; }
  .brand--small .brand__mark { width: 10px; height: 10px; border-radius: 50%; background: var(--brand-blue); }

  .cover-photo { position: absolute; left: 0; top: 0; width: 600px; height: 566px;
                 background: linear-gradient(120deg, var(--photo-light) 0%, #dde2e8 45%, var(--photo-mid) 100%); }

  .headline { position: absolute; left: 22px; top: 380px; font-family: "Anton", Impact, sans-serif;
              line-height: 0.95; text-transform: uppercase; font-weight: 400; }
  .headline__big { display: block; color: var(--brand-blue); font-size: 80px; letter-spacing: -2px; }
  .headline__small { display: block; color: var(--ink); font-size: 42px; margin-top: 2px; letter-spacing: -1px;
                     text-shadow: 2px 0 0 var(--white), -2px 0 0 var(--white), 0 2px 0 var(--white), 0 -2px 0 var(--white); }

  .tagline { position: absolute; left: 0; top: 590px; width: 600px; text-align: center;
             font-family: "Cinzel", Georgia, serif; font-size: 22px; color: var(--brand-blue); letter-spacing: 0.5px; }

  .details-band { position: absolute; left: 0; top: 640px; width: 600px; height: 96px; background: var(--lime); color: var(--ink); }
  .rsvp-short { position: absolute; left: 24px; top: 30px; font-size: 11.5px; line-height: 1.55; }
  .meeting-details { position: absolute; right: 52px; top: 10px; text-align: right; font-size: 17px; line-height: 1.2; }
  .meeting-details__title { text-transform: uppercase; }
  sup { font-size: 0.6em; line-height: 0; }

  .rsvp-form { position: absolute; left: 0; top: 748px; width: 600px; display: flex; justify-content: center;
               align-items: center; gap: 14px; font-size: 11px; color: var(--ink); white-space: nowrap; }
  .rsvp-form__field { display: flex; align-items: center; gap: 5px; }
  .rsvp-form__box { width: 11px; height: 11px; border: 1px solid var(--ink); }
  .rsvp-form__blank { display: inline-block; border-bottom: 1px solid var(--ink); height: 12px; }
  .rsvp-form__blank--name { width: 110px; }
  .rsvp-form__blank--count { width: 34px; }

  .agenda-chart { position: absolute; left: 84px; top: 90px; width: 460px; height: 345px; }

  .agenda-title { position: absolute; left: 128px; top: 136px; font-weight: 300; font-size: 26px;
                  color: var(--soft-blue); letter-spacing: 0.5px; }
  .agenda-item { position: absolute; background: var(--lime); color: var(--ink); font-size: 16px; line-height: 1.2; padding: 10px 10px; }
  .agenda-item--reception { left: 130px; top: 174px; width: 212px; height: 54px; }
  .agenda-item--training { left: 232px; top: 274px; width: 226px; height: 80px; }
  .agenda-item__caps { text-transform: uppercase; }

  .agenda-copy { position: absolute; left: 78px; top: 432px; width: 462px; font-size: 14.4px; line-height: 1.22;
                 color: var(--soft-blue); }
  .expenses-note { position: absolute; left: 78px; top: 520px; width: 462px; font-size: 10.5px; line-height: 1.3;
                   color: var(--ink); }
  .expenses-note strong { font-weight: 600; }

  .venue-photo { position: absolute; left: 114px; top: 584px; width: 205px; height: 132px;
                 background: linear-gradient(180deg, #4a6fb0 0%, #6d8fc7 45%, #b58a5c 70%, #8a8d8f 100%); }
  .venue-card { position: absolute; left: 325px; top: 584px; width: 187px; height: 132px; background: var(--location-blue);
                color: var(--white); font-size: 11.5px; line-height: 1.45; padding: 22px 16px 0; }
  .venue-card__title { text-transform: uppercase; margin-bottom: 8px; }
  .venue-card__shuttle { margin-top: 8px; font-weight: 600; }

  .rsvp-line { position: absolute; left: 110px; top: 730px; font-size: 11.5px; color: var(--ink); white-space: nowrap; }
  .rsvp-line span + span { margin-left: 12px; }
</style>
</head>
<body>
<main class="spread">

  <section class="page page--cover">
    <div class="cover-photo" role="img" aria-label="Photo of three smiling business professionals seated at a meeting table"></div>

    <div class="brand brand--lead" style="left:24px; top:40px;"><span class="brand__mark"></span>Corvell Vendor Solutions</div>

    <h1 class="headline">
      <span class="headline__big">Most</span>
      <span class="headline__big">Important</span>
      <span class="headline__small">Event in 5 Years</span>
    </h1>

    <p class="tagline">Do not even consider missing it</p>

    <div class="details-band">
      <p class="rsvp-short">Fax RSVP to 775-555-0143<br>Email : marcuso@corvellhq.example</p>
      <div class="meeting-details">
        <p class="meeting-details__title">Details of Sales Meeting</p>
        <p>Nov 10<sup>th</sup> - 11<sup>th</sup> in Dallas, TX</p>
        <p>Nov 10<sup>th</sup> (welcome party) 7-9pm</p>
      </div>
    </div>

    <form class="rsvp-form" aria-label="RSVP">
      <span class="rsvp-form__field">Name <span class="rsvp-form__blank rsvp-form__blank--name"></span></span>
      <span class="rsvp-form__field"><span class="rsvp-form__box"></span>YES! I will gladly attend. <span class="rsvp-form__blank rsvp-form__blank--count"></span> # attending</span>
      <span class="rsvp-form__field"><span class="rsvp-form__box"></span>Can't make it.</span>
    </form>
  </section>

  <section class="page page--agenda">
    <div class="brand brand--lead" style="left:20px; top:46px;"><span class="brand__mark"></span>Corvell Vendor Solutions</div>

    <svg class="agenda-chart" viewBox="0 0 460 345" aria-hidden="true">
      <g fill="var(--chart-bar)">
        <rect x="0" y="310" width="44" height="35"/>
        <rect x="68" y="288" width="44" height="57"/>
        <rect x="136" y="262" width="44" height="83"/>
        <rect x="204" y="222" width="44" height="123"/>
        <rect x="272" y="182" width="44" height="163"/>
        <rect x="340" y="125" width="44" height="220"/>
        <rect x="408" y="105" width="48" height="240"/>
      </g>
      <path d="M0 325 C 150 245, 300 155, 420 22" fill="none" stroke="var(--chart-arrow)" stroke-width="8"/>
      <path d="M400 16 L440 2 L432 42 Z" fill="var(--chart-arrow)"/>
    </svg>

    <h2 class="agenda-title">PRELIMINARY AGENDA</h2>

    <div class="agenda-item agenda-item--reception">
      <p>Nov, 10<sup>th</sup> 7-9pm</p>
      <p class="agenda-item__caps">Welcome Reception</p>
    </div>

    <div class="agenda-item agenda-item--training">
      <p>Nov 11<sup>th</sup> and 12<sup>th</sup> 9-4</p>
      <p class="agenda-item__caps">Cardwise Drill Week</p>
      <p class="agenda-item__caps">Sales Training</p>
    </div>

    <p class="agenda-copy">Learn the tools you need to become more relevant in the marketplace as we launch multiple new cutting edge products and services. Many vendors will be on hand to personally meet you and provide the tools and marketing information you need.</p>

    <p class="expenses-note"><strong>***</strong> This event is so important our CEO, Marcus Odrey has decided that we are covering all of the expenses! That's right, we will provide the sleeping room based on double occupancy, all meals, and with 10 deals in 90 days we will even reimburse your airfare if a flight is necessary.</p>

    <div class="venue-photo" role="img" aria-label="Photo of the conference hotel exterior at dusk"></div>
    <div class="venue-card">
      <p class="venue-card__title">Location of Event</p>
      <p>Northgate Harbor Inn East</p>
      <p>2870 Lanterly Pkwy.</p>
      <p>Fort Worth, TX 76192</p>
      <p class="venue-card__shuttle">FREE Shuttle from NHE!</p>
    </div>

    <p class="rsvp-line"><span>Fax RSVP to 775-555-0143</span><span>Email : marcuso@corvellhq.example</span></p>
    <div class="brand brand--small" style="left:494px; top:731px;"><span class="brand__mark"></span>Bristane Ledger</div>
  </section>

</main>
</body>
</html>
```